Zielgruppe
Branche: Logistik/Spedition
Spezifisch: Fahrzeugüberführung und weitere Dienstleistungen in der Branche siehe Webseite
Zielgruppe: Autohäuser, Leasinggesellschaften, Autovermietungen, Firmen mit eigenem Fuhrpark
Aufgabenstellung
Es handelt sich hierbei um ein Portfolio, welches als E-Mail Anhang an potentielle Kunden zugeschickt oder bei Anfragen per E-Mail mitgeschickt werden soll. Dieses Portfolio wünschen wir in Form einer PDF-Datei.
-Grafische, textliche und inhaltliche Orientierung an unserer Homepage
-alle Dienstleistungen sollen im Portfolio beschrieben werden
-Hauptdienstleistungen, die ausführlicher beschrieben werden sollen: Eigenachsüberfürhung (Hauptdienstleistung)

```html
<!DOCTYPE html>
<html lang="de">
<head>
<meta charset="utf-8">
<title>RELAM Fleetservices – Portfolio</title>
<link href="https://fonts.googleapis.com/css2?family=Oswald:wght@500;600&family=Poppins:wght@400;600&display=swap" rel="stylesheet">
<style>
:root{
  --blue:#2f9fe0;
  --title-blue:#3a8dd4;
  --ink:#111;
  --text:#5a5a5a;
  --aside:#f3f3f4;
  --rule:#dcdcdc;
  --white:#fff;
}
*{margin:0;padding:0;box-sizing:border-box}
html,body{width:1200px;height:2450px;overflow:hidden;background:var(--white)}
body{position:relative;font-family:"Poppins",sans-serif;color:var(--text)}
.page{position:absolute;width:333px;height:236px;background:var(--white);box-shadow:0 2px 7px rgba(0,0,0,.28);overflow:hidden}
.col-l{left:172px}.col-r{left:642px}
.photo{position:absolute;left:0;top:0;width:100%;height:57px}
.brand-tab{position:absolute;right:0;top:0;width:98px;height:57px;background:#000;clip-path:polygon(24% 0,100% 0,100% 100%,0 100%)}
.brand-tab .logo{position:absolute;right:14px;top:13px}
.brand-tab .url{position:absolute;right:14px;top:34px;font-size:3.6px;color:var(--white);font-weight:600}
.brand-tab .url b{color:var(--blue)}
.logo{font-family:"Oswald",sans-serif;font-weight:600;color:var(--blue);font-size:10px;letter-spacing:.08em;display:flex;align-items:center;gap:3px;line-height:1}
.logo i{display:block;width:4px;height:4px;background:var(--blue)}
.edge{position:absolute;right:0;top:0;width:6px;height:78px;background:var(--blue)}
.aside{position:absolute;left:150px;top:57px;right:0;bottom:5px;background:var(--aside)}
.foot{position:absolute;left:0;right:0;bottom:0;height:5px;background:var(--ink)}
.foot::after{content:"";position:absolute;right:0;top:0;width:26%;height:100%;background:var(--blue)}
.main{position:absolute;left:34px;top:76px;width:108px}
.title{font-family:"Oswald",sans-serif;font-weight:500;color:var(--title-blue);font-size:9.4px;line-height:1.5;text-transform:uppercase;margin-bottom:6px}
.copy{font-size:3.2px;line-height:1.65;color:var(--text);margin-bottom:4px}
.sub{font-family:"Oswald",sans-serif;font-weight:600;font-size:4.2px;color:var(--ink);text-transform:uppercase;line-height:1.5;margin-bottom:4px}
.side{position:absolute;left:168px;top:76px;width:142px}
.side .sub{margin-bottom:6px}
.ticks{list-style:none}
.ticks li{position:relative;font-size:3.2px;line-height:1.55;padding:2px 0 2px 8px;border-bottom:.5px solid var(--rule)}
.ticks li::before{content:"";position:absolute;left:0;top:2.6px;width:3.4px;height:3.4px;border:.5px solid var(--blue)}
.ticks li b{display:block;color:var(--ink);font-weight:600}
.toc{list-style:none}
.toc li{display:flex;justify-content:space-between;font-size:3.3px;padding:2.5px 0;border-bottom:.5px solid var(--rule)}
.caption{position:absolute;left:34px;top:46px;width:128px;height:28px;background:#000;clip-path:polygon(0 0,100% 0,90% 100%,0 100%);color:var(--white);font-size:4.2px;font-weight:600;text-align:center;line-height:1.35;padding:6px 16px 0 6px}
.thumb{position:absolute;left:34px;top:136px;width:78px;height:82px}
.steps{display:flex;flex-direction:column;gap:5px}
.step{background:var(--white);border:.5px solid var(--rule);padding:4px 5px 4px 20px;position:relative;min-height:26px}
.step .num{position:absolute;left:5px;top:4px;width:11px;height:11px;background:var(--blue);color:var(--white);font-size:4.4px;font-weight:600;display:flex;align-items:center;justify-content:center}
.step .sub{margin-bottom:2px;font-size:3.7px}
.step .copy{margin:0}
/* covers */
.cover{background:#000}
.cover .hero{position:absolute;right:0;top:0;width:205px;height:188px;clip-path:polygon(30% 0,100% 0,100% 100%,0 100%)}
.cover .sheet{position:absolute;right:0;bottom:0;width:200px;height:60px;background:var(--white);clip-path:polygon(12% 0,100% 0,100% 100%,0 100%)}
.cover .logo{position:absolute;left:16px;top:44px;font-size:22px}
.cover .logo i{width:7px;height:7px}
.cover .headline{position:absolute;left:16px;top:90px;width:150px;font-family:"Oswald",sans-serif;font-weight:600;color:var(--white);font-size:12.5px;line-height:1.5;text-transform:uppercase}
.cover .lead{position:absolute;left:16px;top:66px;width:140px;font-size:3.4px;line-height:1.6;color:#ddd}
.cover .address{position:absolute;left:16px;top:178px;font-size:3.3px;line-height:1.6;color:var(--white);font-weight:600}
.cover .contact{position:absolute;right:16px;bottom:14px;display:flex;gap:10px;font-family:"Oswald",sans-serif;font-size:4.2px;color:var(--ink);font-weight:500;align-items:center}
.cover .contact span{display:flex;align-items:center;gap:2px}
.badge{position:absolute;left:258px;top:158px;width:28px;height:24px;background:#eee;border-radius:2px}
</style>
</head>
<body>

<!-- Cover -->
<section class="page cover col-l" style="top:156px">
  <div class="hero" role="img" aria-label="Foto: junge Frau am Steuer eines Autos" style="background:linear-gradient(120deg,#b8a28c,#e9e2d8 55%,#f6f4f0)"></div>
  <div class="badge"></div>
  <div class="sheet"></div>
  <div class="logo"><i></i>RELAM</div>
  <h1 class="headline">Sie brauchen eine Fahrzeugüberführung?</h1>
  <p class="address">RELAM GmbH<br><br>Lindenweg 12<br>10115 Berlin<br><br>Mo–Fr: 8:00 – 18:00<br>Sa–So: geschlossen</p>
  <div class="contact">
    <span><svg width="5" height="5" viewBox="0 0 10 10"><circle cx="5" cy="5" r="4" fill="none" stroke="#111"/></svg>WWW.RELAM.GMBH</span>
    <span><svg width="6" height="5" viewBox="0 0 12 10"><rect x="1" y="1" width="10" height="8" fill="none" stroke="#111"/><path d="M1 1l5 4 5-4" fill="none" stroke="#111"/></svg>INFO@RELAM.GMBH</span>
    <span><svg width="5" height="5" viewBox="0 0 10 10"><path d="M2 1l2 0 1 2-1 1c1 2 2 3 3 3l1-1 2 1 0 2c-5 0-8-3-8-8z" fill="#111"/></svg>030 55 01 23 4-0</span>
  </div>
</section>

<!-- Page 2: Inhalt -->
<section class="page col-l" style="top:433px">
  <div class="photo" role="img" aria-label="Foto: Autobahn mit Verkehr" style="background:linear-gradient(90deg,#6f7d52,#b7b7a6 40%,#8e8f86 70%,#5d6150)"></div>
  <div class="brand-tab"><div class="logo"><i></i>RELAM</div><div class="url">www.relam.gmbh <b>| 2</b></div></div>
  <div class="aside"></div>
  <div class="main">
    <h2 class="title">Fahrzeugüberführung – unser Service für Ihre Autoüberführung</h2>
    <p class="copy">Die RELAM GmbH ist einer der führenden Unternehmen im Bereich Fahrzeugüberführung. Wir führen jährlich mehrere Zehntausend Eigenachsüberführungen durch, sowohl für private als auch für viele namhafte Kunden. Diese Position haben wir uns durch zuverlässigen und kundenorientierten Service erarbeitet. Fragen Sie direkt Ihre gewünschten Leistungen an und profitieren Sie von unserer Erfahrung und Expertise.</p>
  </div>
  <div class="side">
    <h3 class="sub">Inhalt</h3>
    <ul class="toc">
      <li><span>Eigenachsüberführung</span><span>3</span></li>
      <li><span>Fremdachsenüberführung</span><span>6</span></li>
      <li><span>Stellplätze &amp; Platzdienstleistungen</span><span>7</span></li>
      <li><span>Fahrzeugaufbereitung</span><span>8</span></li>
      <li><span>Reifenhandling</span><span>9</span></li>
      <li><span>Werkstattfahrten</span><span>10</span></li>
      <li><span>Zulassungsdienst</span><span>11</span></li>
      <li><span>Anhängerüberführung</span><span>12</span></li>
      <li><span>Autotransport</span><span>13</span></li>
      <li><span>Fahrzeugtransport</span><span>14</span></li>
    </ul>
  </div>
  <div class="foot"></div>
</section>

<!-- Page 3 -->
<section class="page col-l" style="top:708px">
  <div class="photo" role="img" aria-label="Foto: Landstraße bei Sonnenuntergang" style="background:linear-gradient(90deg,#c79a6a,#7c6a58 45%,#4a4a48)"></div>
  <div class="brand-tab"><div class="logo"><i></i>RELAM</div><div class="url">www.relam.gmbh <b>| 3</b></div></div>
  <div class="edge"></div>
  <div class="aside"></div>
  <div class="caption">Zuverlässig ans Ziel mit einer Fahrzeugüberführung vom Experten.</div>
  <div class="main" style="top:98px"><h2 class="title">Fahrzeugüberführung auf eigener Achse</h2></div>
  <div class="thumb" role="img" aria-label="Foto: Hand bedient eine App auf dem Smartphone" style="background:linear-gradient(135deg,#2c4a6e,#8aa6c4 60%,#c9d6e2)"></div>
  <div class="side">
    <h3 class="sub">Bundes- und europaweite Überführung von Fahrzeugen durch kompetente Experten</h3>
    <p class="copy">Die Abholung von Fahrzeugen vom Autohändler, die Überführung von Mietfahrzeugen an einen anderen Standort, der Transport eines besonders wertvollen Elektroautos: Wann immer ein Fahrzeug sicher überführt werden soll, fehlen oft die zeitlichen oder personellen Ressourcen. Genau hier unterstützen wir Sie mit erfahrenen Fahrern.</p>
    <h3 class="sub" style="margin-top:5px">Fahrzeugüberführung auf eigener Achse – einfach und sicher mit Unterstützung der RELAM GmbH</h3>
    <p class="copy">Alle Fahrzeugüberführungen auf eigener Achse werden bei der RELAM GmbH von sorgfältig ausgewählten und eingehend geschulten Mitarbeitern ausgeführt. Wir bieten unseren Service sowohl für zugelassene als auch für nicht zugelassene Fahrzeuge an und überführen diese pünktlich und sicher an den gewünschten Zielort.</p>
  </div>
  <div class="foot"></div>
</section>

<!-- Page 4 -->
<section class="page col-l" style="top:980px">
  <div class="photo" role="img" aria-label="Foto: Hände am Tablet und Fahrzeuginnenraum" style="background:linear-gradient(90deg,#c8d3de,#9aa7b3 45%,#3c3f44)"></div>
  <div class="brand-tab"><div class="logo"><i></i>RELAM</div><div class="url">www.relam.gmbh <b>| 4</b></div></div>
  <div class="edge"></div>
  <div class="aside"></div>
  <div class="caption">Profitieren Sie mit unserem europaweiten Service zur Autoüberführung.</div>
  <div class="main" style="top:98px"><h2 class="title">Fahrzeugüberführung auf eigener Achse</h2></div>
  <div class="thumb" role="img" aria-label="Foto: lächelnder Fahrer vor einem Transporter" style="background:linear-gradient(160deg,#d8dce0,#8b8f94 55%,#4d5560)"></div>
  <div class="side">
    <h3 class="sub">Profitieren Sie mit der RELAM GmbH von wichtigen Vorteilen</h3>
    <ul class="ticks">
      <li><b>Transparente Preise</b>Bereits bei Ihrer Anfrage werden Ihnen in Echtzeit alle Kosten angezeigt.</li>
      <li><b>Zuverlässige Fahrer</b>Für die Überführungen setzen wir erfahrene und regelmäßig geschulte Fahrer ein.</li>
      <li><b>Langjährige Erfahrung</b>Die RELAM GmbH ist seit 2009 als Dienstleister für Fahrzeugüberführungen tätig.</li>
      <li><b>Eigene App</b>Für noch besseren Service haben wir eine eigene App entwickelt.</li>
      <li><b>Starkes Kundenportal</b>Mit unserem Kundenportal behalten Sie jede Überführung stets im Blick.</li>
      <li><b>Fahrzeugzustellungen</b>Fahrzeugzustellungen an den Endnutzer auf Wunsch auch mit Einweisung.</li>
    </ul>
  </div>
  <div class="foot"></div>
</section>

<!-- Page 5 -->
<section class="page col-l" style="top:1255px">
  <div class="photo" role="img" aria-label="Foto: Blick aus dem Auto auf eine sonnige Straße" style="background:linear-gradient(90deg,#d9a55c,#8a8577 45%,#5b6a7a)"></div>
  <div class="brand-tab"><div class="logo"><i></i>RELAM</div><div class="url">www.relam.gmbh <b>| 5</b></div></div>
  <div class="edge"></div>
  <div class="aside"></div>
  <div class="caption">Die RELAM GmbH überzeugt mit starken Leistungen im Bereich der Fahrzeugüberführung.</div>
  <div class="main" style="top:98px"><h2 class="title">Fahrzeugüberführung auf eigener Achse</h2></div>
  <div class="thumb" role="img" aria-label="Foto: Hände auf einer Laptop-Tastatur" style="background:linear-gradient(135deg,#e2e4e7,#a4a8ad 60%,#6e7379)"></div>
  <div class="side">
    <h3 class="sub">Der Ablauf der Fahrzeugüberführung auf eigener Achse im Überblick</h3>
    <div class="steps">
      <div class="step"><span class="num">01</span><h4 class="sub">Anfrage &amp; Auftragserteilung</h4><p class="copy">Stellen Sie einfach eine Anfrage über unsere Homepage und wählen Sie die passende Variante der Überführung aus.</p></div>
      <div class="step"><span class="num">02</span><h4 class="sub">Fahrzeugübernahme &amp; Zustandsprüfung</h4><p class="copy">Zum vereinbarten Termin wird das Fahrzeug abgeholt und eine genaue Zustandsprüfung durchgeführt.</p></div>
      <div class="step"><span class="num">03</span><h4 class="sub">Fahrzeugüberführung &amp; Übergabe</h4><p class="copy">Ihr Fahrzeug wird auf einer sorgfältig geplanten Route zum Zielort gebracht und dort übergeben.</p></div>
    </div>
  </div>
  <div class="foot"></div>
</section>

<!-- Page 6 -->
<section class="page col-l" style="top:1531px">
  <div class="photo" role="img" aria-label="Foto: Fahrer prüft ein Fahrzeug" style="background:linear-gradient(90deg,#aeb7c0,#e3e6ea 40%,#7c8590)"></div>
  <div class="brand-tab"><div class="logo"><i></i>RELAM</div><div class="url">www.relam.gmbh <b>| 6</b></div></div>
  <div class="aside"></div>
  <div class="main">
    <h2 class="title">Fahrzeugüberführung auf fremder Achse</h2>
    <p class="copy">Ob abgemeldet, nicht fahrbereit oder zusätzliche Kilometer unerwünscht – mit unseren Autotransportern bringen wir Ihre Fahrzeuge sicher und zuverlässig ans Ziel. Vor der Beladung wird jedes Fahrzeug durch unsere geschulten Fahrer einer sorgfältigen Zustandsprüfung unterzogen und im Protokoll festgehalten.</p>
  </div>
  <div class="side">
    <h3 class="sub">Profitieren Sie von unseren Leistungen – Fahrzeugüberführung auf fremder Achse</h3>
    <ul class="ticks">
      <li>Überführung von An- und abgemeldeten Fahrzeugen</li>
      <li>Bereitstellung in ganz Deutschland und europaweit</li>
      <li>Zugang zum Kundenportal für absolute Transparenz</li>
      <li>Neu- und Leasingfahrzeuge</li>
      <li>Fahrzeugzustellung an den Endnutzer mit Einweisung</li>
      <li>Zuverlässige und flexible Handlungsmöglichkeiten durch schnelle Reaktionszeiten</li>
      <li>Kompetente und freundliche Auskunft über Ihren Auftragsstatus</li>
      <li>Sicherheit: ausgebildete sowie erfahrene Fahrer mit umfassendem Versicherungsschutz</li>
    </ul>
  </div>
  <div class="foot"></div>
</section>

<!-- Page 7 -->
<section class="page col-l" style="top:1802px">
  <div class="photo" role="img" aria-label="Foto: Parkhaus mit abgestellten Fahrzeugen" style="background:linear-gradient(90deg,#c55a3c,#8e9aa6 35%,#b7bfc8 65%,#c55a3c)"></div>
  <div class="brand-tab"><div class="logo"><i></i>RELAM</div><div class="url">www.relam.gmbh <b>| 7</b></div></div>
  <div class="aside"></div>
  <div class="main">
    <h2 class="title">Stellplätze &amp; Platzdienstleistungen</h2>
    <p class="copy">Mit über 200 überdachten Dauer- oder Tagesstellplätzen bieten wir Ihnen sichere und rechtzeitig geplante Abstellplätze für Ihre Fahrzeuge an. Durch unsere Platzdienstleistungen bieten wir Ihnen den zusätzlichen Service an, Ihre Neu- oder Gebrauchtfahrzeuge in einem unserer Stellplätze zu lagern und abholen zu lassen.</p>
    <p class="copy">Bei Anlieferung von Neufahrzeugen wird im Einzelnen und mit Sorgfalt geprüft, ob das Fahrzeug Schäden oder eventuelle Fehlteile aufweist. Auch Gebrauchtfahrzeuge werden auf Beschädigungen geprüft und das Ergebnis in einer Checkliste schriftlich festgehalten.</p>
  </div>
  <div class="side">
    <h3 class="sub">Profitieren Sie von unseren Leistungen – Stellplätze &amp; Platzdienstleistungen</h3>
    <ul class="ticks">
      <li>Beaufsichtigung von Instandsetzungen und Wartungen und Bereitstellung einer überdachten Parkfläche.</li>
      <li>Anlieferung und Check-Up von Neu- oder Gebrauchtfahrzeugen zur Prüfung von Zustand und Sicherheit.</li>
      <li>Professioneller, sicherer Hin- und Rücktransport von Fahrzeugen – auch für Hauptuntersuchungen.</li>
      <li>Auslieferung von Neufahrzeugen an den Endnutzer – pünktliche Übergabe ganz nach Kundenwunsch.</li>
    </ul>
  </div>
  <div class="foot"></div>
</section>

<!-- Page 8 -->
<section class="page col-l" style="top:2073px">
  <div class="photo" role="img" aria-label="Foto: Hand poliert ein Auto mit blauem Tuch" style="background:linear-gradient(90deg,#4a5058,#9aa3ab 45%,#6fb3de 70%,#c9ced3)"></div>
  <div class="brand-tab"><div class="logo"><i></i>RELAM</div><div class="url">www.relam.gmbh <b>| 8</b></div></div>
  <div class="aside"></div>
  <div class="main">
    <h2 class="title">Fahrzeugaufbereitung Rundumsorglospaket</h2>
    <h3 class="sub">Unser Angebot für Sie</h3>
    <ul class="ticks">
      <li>Handwäsche inkl. Felgen</li>
      <li>Basispflege</li>
      <li>Premiumpflege</li>
      <li>Basis-Innenraumpflege ohne Außenwäsche</li>
      <li>Premium-Innenraumpflege ohne Außenwäsche</li>
      <li>Rundumsorglospaket</li>
      <li>Lackaufbereitung</li>
      <li>Leasingrücknahme</li>
    </ul>
  </div>
  <div class="side">
    <h3 class="sub">Profitieren Sie von unseren Leistungen – Fahrzeugaufbereitung Rundumsorglospaket</h3>
    <ul class="ticks">
      <li>Alle Fahrzeuge, die wir bewegen, sind über uns vollkasko-versichert.</li>
      <li>Zuverlässigkeit: Wir sind stets bemüht, die Erwartungen aller Kunden zu erfüllen oder zu übertreffen.</li>
      <li>Schnelle Bearbeitung: Optimierte Prozesse ermöglichen eine flexible und schnelle Bearbeitung Ihrer Aufträge.</li>
      <li>Unser Onlineportal ermöglicht eine komfortable Auftragsvergabe, Protokollierung und Nachverfolgung.</li>
    </ul>
  </div>
  <div class="foot"></div>
</section>

<!-- Page 9 -->
<section class="page col-r" style="top:156px">
  <div class="photo" role="img" aria-label="Foto: Mechaniker mit Autoreifen" style="background:linear-gradient(90deg,#b88455,#d9c6b0 35%,#3d3a38 60%,#a86f48)"></div>
  <div class="brand-tab"><div class="logo"><i></i>RELAM</div><div class="url">www.relam.gmbh <b>| 9</b></div></div>
  <div class="aside"></div>
  <div class="main">
    <h2 class="title">Reifenhandling: zeitnah, sicher und pünktlich</h2>
    <p class="copy">Hol- und Bringservice zur Werkstatt, ob Reparatur oder Reifenhandling. Wir vereinbaren für Sie zeitnah einen Termin, bringen Ihr Fahrzeug sicher und pünktlich in die Werkstatt und anschließend zu Ihnen zurück. Wenn es um Autoglasreparaturen oder kleine Smart Repairs vor der Rückgabe Ihres Leasingfahrzeugs geht, sind Sie bei uns an der richtigen Adresse. Sie profitieren stets von Preisnachlässen unserer Kooperationspartner.</p>
  </div>
  <div class="side">
    <h3 class="sub">Profitieren Sie von unseren Leistungen – Reifenhandling</h3>
    <ul class="ticks">
      <li>Terminvereinbarungsservice: Setzen Sie sich mit uns in Verbindung – wir sprechen mit Ihnen alle Details durch.</li>
      <li>Preisnachlass bei Kooperationspartnern: Sie sparen Zeit und Geld und profitieren von Preisnachlässen.</li>
      <li>Zeitnah, sicher und pünktlich: Ihr Fahrzeug ist schnell wieder zur Verfügung.</li>
      <li>Hol- und Bringservice: Alle Fahrten inklusive – wir bringen Ihr Fahrzeug zur Werkstatt und holen es ab.</li>
    </ul>
  </div>
  <div class="foot"></div>
</section>

<!-- Page 10 -->
<section class="page col-r" style="top:433px">
  <div class="photo" role="img" aria-label="Foto: Mechaniker arbeitet am Motorraum" style="background:linear-gradient(90deg,#c9ced4,#8c96a2 45%,#2f3f5c 70%,#b8c0c8)"></div>
  <div class="brand-tab"><div class="logo"><i></i>RELAM</div><div class="url">www.relam.gmbh <b>| 10</b></div></div>
  <div class="aside"></div>
  <div class="main">
    <h2 class="title">Werkstattfahrten: Hol- und Bringservice</h2>
    <p class="copy">Hol- und Bringservice zur Werkstatt, ob Reparatur oder Reifenhandling. Wir vereinbaren für Sie zeitnah einen Termin, bringen Ihr Fahrzeug sicher und pünktlich in die Werkstatt und anschließend zu Ihnen zurück. Wenn es um Autoglasreparaturen oder kleine Smart Repairs vor der Rückgabe Ihres Leasingfahrzeugs geht, sind Sie bei uns genau richtig. Sie profitieren stets von Preisnachlässen unserer Kooperationspartner.</p>
  </div>
  <div class="side">
    <h3 class="sub">Profitieren Sie von unseren Leistungen – Hol- und Bringservice</h3>
    <ul class="ticks">
      <li>Terminvereinbarungsservice: Individuelle &amp; kurzfristige Planung – rufen Sie uns an und wir finden einen Termin.</li>
      <li>Preisnachlass bei Kooperationspartnern: Ihr Spezialist für Werkstattfahrten – nutzen Sie unsere Vorteile.</li>
      <li>Zeitnah, sicher und pünktlich: Dank pünktlicher Ankunft an der Werkstatt sind alle Arbeiten schnell erledigt.</li>
      <li>Hol- und Bringservice: Abwicklung aller Fahrten – wir übernehmen den Transport zur Werkstatt und zurück.</li>
    </ul>
  </div>
  <div class="foot"></div>
</section>

<!-- Page 11 -->
<section class="page col-r" style="top:708px">
  <div class="photo" role="img" aria-label="Foto: Mechaniker unter geöffneter Motorhaube" style="background:linear-gradient(90deg,#5c6670,#a9b2bb 40%,#3c5a8a 65%,#8a9097)"></div>
  <div class="brand-tab"><div class="logo"><i></i>RELAM</div><div class="url">www.relam.gmbh <b>| 11</b></div></div>
  <div class="aside"></div>
  <div class="main">
    <h2 class="title">Zulassungsdienst: bundesweit und kostengünstig</h2>
    <p class="copy">Wir bieten Ihnen bundesweit günstigen und zuverlässigen Kfz-Zulassungsdienst an – ganz egal, ob es sich um ein Neu- oder Gebrauchtwagen handelt. Bei Aus- oder Einfuhr von Nicht-EU-Fahrzeugen erledigen wir alle Formalitäten und sorgen für notwendige Zollabwicklung sowie Ausfuhrkennzeichen.</p>
    <p class="copy">Dadurch, dass wir sämtliche Formalien für Sie übernehmen, sparen Sie Zeit und ersparen sich aufwendige Behördengänge sowie lange Wartezeiten.</p>
  </div>
  <div class="side">
    <h3 class="sub">Profitieren Sie von unseren Leistungen – Zulassungsdienst</h3>
    <ul class="ticks">
      <li>Regionale und bundesweite Fahrzeugzulassung</li>
      <li>Fahrzeugabmeldung</li>
      <li>Kfz-Kennzeichenprägung</li>
      <li>Ausfertigung von Exportpapieren</li>
      <li>24-Stunden-Service bei sämtlichen regionalen und zulassungsrelevanten Leistungen</li>
      <li>Erstellung der Ausfuhrdokumente für die Abwicklung beim Zoll</li>
      <li>Umfassende Beratung – auch in außergewöhnlichen Fällen</li>
      <li>Abholung und Auslieferung</li>
    </ul>
  </div>
  <div class="foot"></div>
</section>

<!-- Page 12 -->
<section class="page col-r" style="top:980px">
  <div class="photo" role="img" aria-label="Foto: Auto mit Wohnanhänger auf der Straße" style="background:linear-gradient(90deg,#6f7f5c,#d8d6d0 40%,#a8323a 65%,#5a5e62)"></div>
  <div class="brand-tab"><div class="logo"><i></i>RELAM</div><div class="url">www.relam.gmbh <b>| 12</b></div></div>
  <div class="aside"></div>
  <div class="main">
    <h2 class="title">Anhängerüberführung bis zu 750 kg</h2>
    <p class="copy">Bis zu 750 kg bzw. einer zulässigen Gesamtmasse von 3,5 t überführen wir Ihren Anhänger mit eigenem Zugfahrzeugen. Sollte ein entsprechendes Zugfahrzeug zur Verfügung gestellt werden, überführen wir selbstverständlich auch größere Gespanne.</p>
    <p class="copy">Um Anhängerüberführungen einzuplanen, benötigen wir in der Regel eine Vorlaufzeit von fünf Werktagen. Wir übernehmen keine Haftung für die Beladung. Der Kunde muss vorher eine Ladungssicherheit gewährleisten.</p>
  </div>
  <div class="side">
    <h3 class="sub">Profitieren Sie von unseren Leistungen – Anhängerüberführung</h3>
    <ul class="ticks">
      <li>Anhänger bis zu 750 kg / Gesamtmasse bis zu 3,5 t</li>
      <li>Eigene Zugfahrzeuge</li>
      <li>Deutschland- und europaweit</li>
      <li>Kurze Vorlaufzeit</li>
    </ul>
  </div>
  <div class="foot"></div>
</section>

<!-- Page 13 -->
<section class="page col-r" style="top:1255px">
  <div class="photo" role="img" aria-label="Foto: weißes Auto auf sonniger Landstraße" style="background:linear-gradient(90deg,#7d8d9c,#c8ccd0 35%,#d89a4a 70%,#f2c27a)"></div>
  <div class="brand-tab"><div class="logo"><i></i>RELAM</div><div class="url">www.relam.gmbh <b>| 13</b></div></div>
  <div class="aside"></div>
  <div class="main">
    <h2 class="title">Autotransportkosten</h2>
    <h3 class="sub">Profitieren Sie von transparenten, günstigen Autotransportkosten und weiteren wichtigen Vorteilen</h3>
    <ul class="ticks">
      <li>Langjährige Erfahrung und fundierte Expertise: Seit 2009 bieten wir als Dienstleister Fahrzeugtransporte in ganz Deutschland an.</li>
      <li>Einzigartiges Kundenportal: Mit unserem Kundenportal haben Sie stets alle wichtigen Aspekte rund um den Transport im Blick.</li>
      <li>Für noch besseren Service haben wir eine eigene App entwickelt.</li>
      <li>Jeder Autotransport auf Eigenachse wird bei uns von erfahrenen und geschulten Fahrern durchgeführt.</li>
      <li>Durchdachtes Qualitätsmanagement: Dafür steht auch unsere Zertifizierung nach ISO 9001:2015.</li>
    </ul>
  </div>
  <div class="side">
    <h3 class="sub">Diese Faktoren können den Schluss-Preis beeinflussen</h3>
    <div class="steps">
      <div class="step"><span class="num">01</span><h4 class="sub">Rote Kennzeichen</h4><p class="copy">Soll dieses von uns vor der Überführung gestellt werden, berechnen wir dafür eine Gebühr.</p></div>
      <div class="step"><span class="num">02</span><h4 class="sub">Zusatzleistungen</h4><p class="copy">Die Preise für Zusatzleistungen werden vor der Buchung angezeigt und auf Wunsch zu den Kosten hinzugefügt.</p></div>
      <div class="step"><span class="num">03</span><h4 class="sub">Zusatzkosten während der Fahrt</h4><p class="copy">Alle bei der Fahrzeugüberführung entstehenden Mehrkosten dokumentieren wir transparent anhand von Belegen.</p></div>
      <div class="step"><span class="num">04</span><h4 class="sub">Wartezeit</h4><p class="copy">Sollten durch Kunden verursachte Wartezeiten entstehen, müssen wir diese ebenfalls bei den Kosten berücksichtigen.</p></div>
    </div>
  </div>
  <div class="foot"></div>
</section>

<!-- Page 14 -->
<section class="page col-r" style="top:1531px">
  <div class="photo" role="img" aria-label="Foto: Blick durch die Windschutzscheibe auf eine Autobahn" style="background:linear-gradient(90deg,#3f3a36,#c9b28f 40%,#e8d9c0 65%,#8d8a84)"></div>
  <div class="brand-tab"><div class="logo"><i></i>RELAM</div><div class="url">www.relam.gmbh <b>| 14</b></div></div>
  <div class="aside"></div>
  <div class="main">
    <h2 class="title">Fahrzeugtransport – die komfortable Lösung für Pkw und mehr</h2>
    <h3 class="sub">Fahrzeugtransport leicht gemacht: wir bringen Ihr Auto schnell, sicher und unkompliziert von A nach B</h3>
    <ul class="ticks">
      <li>Fundierte Expertise: Seit 2009 bieten wir als Dienstleister Fahrzeugtransporte in ganz Deutschland an.</li>
      <li>Ausgebildete Fahrer</li>
      <li>Spezielles Kundenportal</li>
      <li>Für noch besseren Service haben wir eine eigene App entwickelt.</li>
    </ul>
  </div>
  <div class="side">
    <h3 class="sub">Fahrzeugtransport auf fremder Achse: RELAM GmbH macht Sie mobil</h3>
    <p class="copy">Wenn Ihr Fahrzeug nicht mehr fahrbereit ist oder Sie zusätzliche Kilometer vermeiden möchten, bietet sich ein professioneller Fahrzeugtransport auf fremder Achse an.</p>
    <div class="steps" style="margin-top:4px">
      <div class="step"><span class="num">01</span><h4 class="sub">Geschulte Fahrer</h4><p class="copy">Für den Fremdachstransport setzen wir auf speziell ausgebildete und geschulte Fahrer.</p></div>
      <div class="step"><span class="num">02</span><h4 class="sub">Kurze Vorlaufzeiten</h4><p class="copy">Zur ordnungsgemäßen Durchführung benötigen wir je nach Fahrzeug und Gewicht entsprechende Sondertransporter. Dabei halten wir die Vorlaufzeiten so gering wie möglich.</p></div>
      <div class="step"><span class="num">03</span><h4 class="sub">Starker Versicherungsschutz</h4><p class="copy">Für maximale Sicherheit bieten wir in enger Kooperation mit starken Partnern maßgeschneiderte Versicherungsleistungen.</p></div>
    </div>
  </div>
  <div class="foot"></div>
</section>

<!-- Back cover -->
<section class="page cover col-r" style="top:1802px">
  <div class="hero" role="img" aria-label="Foto: lächelnder Mann im Anzug am Steuer" style="background:linear-gradient(120deg,#6b6f75,#c9ccd0 55%,#eef0f2)"></div>
  <div class="sheet"></div>
  <div class="logo" style="top:34px"><i></i>RELAM</div>
  <p class="lead">Wir helfen unseren Kunden dabei, sich auf die wesentlichen Kernpunkte ihrer Arbeit zu fokussieren, indem wir sämtliche Fuhrparkdienstleistungen für Sie übernehmen und damit Kapazitäten für das eigentliche Kerngeschäft unserer Kunden schaffen.<br><br>Wenn Sie sich ein genaueres Bild von unseren Leistungen machen wollen, so nehmen Sie gerne Kontakt zu uns auf.</p>
  <p class="address" style="top:150px">RELAM GmbH<br><br>Lindenweg 12<br>10115 Berlin<br><br>Mo–Fr: 8:00 – 18:00<br>Sa–So: geschlossen</p>
  <div class="contact">
    <span><svg width="5" height="5" viewBox="0 0 10 10"><circle cx="5" cy="5" r="4" fill="none" stroke="#111"/></svg>WWW.RELAM.GMBH</span>
    <span><svg width="6" height="5" viewBox="0 0 12 10"><rect x="1" y="1" width="10" height="8" fill="none" stroke="#111"/><path d="M1 1l5 4 5-4" fill="none" stroke="#111"/></svg>INFO@RELAM.GMBH</span>
    <span><svg width="5" height="5" viewBox="0 0 10 10"><path d="M2 1l2 0 1 2-1 1c1 2 2 3 3 3l1-1 2 1 0 2c-5 0-8-3-8-8z" fill="#111"/></svg>030 55 01 23 4-0</span>
  </div>
</section>

</body>
</html>
```